Marlowe Business Partners Business Card

I'd Like a Two sided Card. Logo was uploaded as an EPS. If you need an additional type, let me know. Colors in Logo are Pantone 289C and Pantone 348C.

I'm thinking of raising the Print on the front, if that matters. Also would like any Vector Art used in the design included with the uploaded files when awarded. If you need any additional info, please let me know. Uploaded card design was for informational purposes only.

The back of the card should be blue, and I like the design included for the back.
Updates

On the Back of the Card, I will probably want my web address. (www.marlowebusinesspartners.example)

Only Square Card Designs Please

Industry/Entity Type

Business

Requirements
Must have
• Should have enough room for longer email addresses in the future.
Nice to have
• email address above WEb URL.

```html
<!DOCTYPE html>
<html lang="en">
<head>
<meta charset="utf-8">
<title>Marlowe Business Partners – Business Card</title>
<link rel="stylesheet" href="https://fonts.googleapis.com/css2?family=Open+Sans:wght@400;600;700&display=swap">
<style>
  :root {
    --navy: #0c2340;
    --green: #138a43;
    --paper: #fbfbfb;
    --paper-back: #f3f3f5;
    --ink-gray: #555a60;
    --stage: #e6e6e6;
  }
  * { margin: 0; padding: 0; box-sizing: border-box; }
  html, body { width: 1200px; height: 1200px; overflow: hidden; }
  body {
    background: var(--stage);
    font-family: "Open Sans", Arial, sans-serif;
    position: relative;
  }
  .card {
    position: absolute;
    left: 266px;
    width: 730px;
    height: 416px;
    overflow: hidden;
    box-shadow: 0 4px 14px rgba(0,0,0,0.25);
  }
  .card-front { top: 106px; background: var(--paper); }
  .card-back { top: 599px; background: var(--paper-back); }

  .front-shapes { position: absolute; inset: 0; }

  .wordmark {
    position: absolute;
    display: flex;
    align-items: center;
    color: var(--navy);
    font-weight: 700;
    text-transform: uppercase;
    white-space: nowrap;
  }
  .card-front .wordmark {
    left: 348px; top: 22px; gap: 10px;
    font-size: 18px; letter-spacing: 0.03em;
  }
  .card-front .wordmark-square { width: 44px; height: 44px; background: var(--navy); flex: none; }

  .person { position: absolute; left: 23px; top: 270px; white-space: nowrap; }
  .person-name { color: var(--green); font-weight: 700; font-size: 30px; line-height: 1.15; }
  .person-role { color: var(--ink-gray); font-size: 20px; text-align: right; margin-top: 2px; }

  .contact {
    position: absolute; left: 350px; top: 122px;
    list-style: none; color: var(--ink-gray); font-size: 15px; line-height: 23px;
    white-space: nowrap;
  }
  .contact li { display: flex; align-items: flex-start; }
  .contact .icon { width: 12px; height: 23px; margin-right: 9px; flex: none; fill: var(--green); }
  .contact .gap { margin-top: 14px; }
  .contact .address span { display: block; }
  .contact .email { font-size: 14.5px; }

  .back-square {
    position: absolute; left: 288px; top: 58px; width: 155px; height: 167px; background: var(--navy);
  }
  .card-back .wordmark {
    left: 0; right: 0; top: 258px; justify-content: center;
    font-size: 38px; letter-spacing: 0.05em;
  }
  .web {
    position: absolute; left: 0; right: 0; top: 372px;
    text-align: center; color: var(--navy); font-size: 17px;
  }
</style>
</head>
<body>
  <section class="card card-front">
    <svg class="front-shapes" width="730" height="416" viewBox="0 0 730 416">
      <path d="M0,0 L228,0 C120,18 30,120 0,254 Z" fill="var(--navy)"/>
      <path d="M0,360 C250,392 716,398 730,186 L730,416 L0,416 Z" fill="var(--green)"/>
      <path d="M0,372 C250,404 720,410 730,200 L730,416 L0,416 Z" fill="var(--navy)"/>
    </svg>

    <div class="wordmark"><span class="wordmark-square"></span>Marlowe Business Partners</div>

    <div class="person">
      <p class="person-name">R. Dana Whitlock</p>
      <p class="person-role">President</p>
    </div>

    <ul class="contact">
      <li class="address">
        <svg class="icon" viewBox="0 0 12 24"><path d="M6,5 C3,5 1,7 1,9.5 C1,13 6,19 6,19 C6,19 11,13 11,9.5 C11,7 9,5 6,5 Z M6,11.5 A2,2 0 1 1 6,7.5 A2,2 0 1 1 6,11.5 Z"/></svg>
        <div><span>2140 Harbor Point Lane</span><span>Linden Grove Market Square</span><span>Fairbrook, VA 20999</span></div>
      </li>
      <li class="gap">
        <svg class="icon" viewBox="0 0 12 24"><path d="M1,10 C1,8 3,7 6,7 C9,7 11,8 11,10 L9,11 L8,9.5 L4,9.5 L3,11 Z M2.5,12 L9.5,12 L10.5,17 L1.5,17 Z"/></svg>
        <span>555.214.3080</span>
      </li>
      <li>
        <svg class="icon" viewBox="0 0 12 24"><path d="M3,6 L9,6 L9,18 L3,18 Z M4,7.5 L4,15.5 L8,15.5 L8,7.5 Z"/></svg>
        <span>555.627.4913</span>
      </li>
      <li>
        <svg class="icon" viewBox="0 0 12 24"><path d="M1,9 L11,9 L11,16 L1,16 Z M1.5,9.5 L6,13 L10.5,9.5" stroke="var(--paper)" stroke-width="0.8"/></svg>
        <span class="email">dwhitlock@marlowebusiness.example</span>
      </li>
    </ul>
  </section>

  <section class="card card-back">
    <div class="back-square"></div>
    <div class="wordmark">Marlowe Business Partners</div>
    <p class="web">www.marlowebusinesspartners.example</p>
  </section>
</body>
</html>
```